Want a package created for a new protein bar

We would like a new package created for a new protein bar project The name of the bar will be VOLMBite a real food protein bar, we would like a ‘window’ on the package of bar like Brave Meadow bar below in images.

VOLMBite
‘Super Food Bar’
14g of Whey Protein
The package film size is the following 12cm width x 15cm Length,
Flavor Peanut Chocolate Chip, additional information will be attached shortly like nutrition facts,

Target Market(s)

fitness market, bodybuilders, athletes, everyday people

Industry/Entity Type

Health Product

Logo Text

VOLMBite

Font styles to use
Serif
Sans Serif
Decorative

Requirements
Must have
• Package window

```html
<!DOCTYPE html>
<html lang="en">
<head>
<meta charset="utf-8">
<title>VOLMBite – Super Food Bar Wrapper</title>
<link rel="stylesheet" href="https://fonts.googleapis.com/css2?family=Archivo:ital,wdth,wght@0,62..125,100..900;1,62..125,100..900&display=swap">
<style>
  :root {
    --bg: #c4c4c4;
    --white: #ffffff;
    --choc: #4e2a1c;
    --band-orange: #ee8a0a;
    --band-red: #c24f2f;
    --flavor: #ee7a45;
    --silver-dark: #a9a9a9;
  }
  * { margin: 0; padding: 0; box-sizing: border-box; }
  html, body { width: 1200px; height: 1109px; overflow: hidden; }
  body {
    background: var(--bg);
    font-family: "Archivo", "Helvetica Neue", Arial, sans-serif;
    position: relative;
  }
  .condensed { font-stretch: 62%; font-variation-settings: "wdth" 62; }
  .brand-mark {
    position: absolute;
    left: 0; right: 0; top: 110px;
    display: flex; justify-content: center; align-items: center; gap: 22px;
  }
  .brand-mark .name {
    color: var(--white);
    font-weight: 800;
    font-size: 150px;
    line-height: 1;
    letter-spacing: -2px;
  }
  .brand-mark .square {
    width: 46px; height: 46px;
    background: var(--band-orange);
  }
  .wrapper {
    position: absolute;
    left: 155px; top: 395px;
    width: 890px; height: 470px;
  }
  .wrapper svg { position: absolute; inset: 0; }
  .wrapper .logo {
    position: absolute;
    left: 168px; top: 120px;
    color: var(--white);
    font-weight: 800;
    font-size: 82px;
    line-height: 1;
    letter-spacing: -1px;
  }
  .wrapper .tagline {
    position: absolute;
    left: 190px; top: 261px;
    color: var(--white);
    font-weight: 800;
    font-stretch: 125%;
    font-variation-settings: "wdth" 125;
    font-size: 36px;
    letter-spacing: 3px;
    line-height: 40px;
    white-space: nowrap;
  }
  .wrapper .flavor {
    position: absolute;
    left: 172px; top: 332px;
    color: var(--flavor);
    font-weight: 900;
    font-style: italic;
    font-size: 20px;
    letter-spacing: 0.5px;
    text-transform: uppercase;
    white-space: nowrap;
    -webkit-text-stroke: 3px var(--white);
    paint-order: stroke fill;
  }
  .wrapper .protein-amount {
    position: absolute;
    left: 170px; top: 378px;
    color: var(--white);
    font-weight: 800;
    font-size: 28px;
    letter-spacing: 3px;
  }
  .wrapper .protein-label {
    position: absolute;
    left: 170px; top: 412px;
    color: var(--white);
    font-weight: 700;
    font-size: 16px;
  }
</style>
</head>
<body>

<header class="brand-mark">
  <span class="name condensed">VOLMBite</span>
  <span class="square"></span>
</header>

<section class="wrapper">
  <svg width="890" height="470" viewBox="0 0 890 470" xmlns="http://www.w3.org/2000/svg">
    <defs>
      <linearGradient id="chocolate-tone" x1="0" y1="0" x2="1" y2="1">
        <stop offset="0" stop-color="#b07a5c"/>
        <stop offset="0.5" stop-color="#6a3a25"/>
        <stop offset="1" stop-color="#4e2a1c" stop-opacity="0"/>
      </linearGradient>
      <linearGradient id="yellow-stripe" x1="0" y1="0" x2="0" y2="1">
        <stop offset="0" stop-color="#f4a81c"/>
        <stop offset="1" stop-color="#f9cf3c"/>
      </linearGradient>
      <linearGradient id="orange-band" x1="0" y1="0" x2="0" y2="1">
        <stop offset="0" stop-color="#f39a10"/>
        <stop offset="0.6" stop-color="#ec8709"/>
        <stop offset="1" stop-color="#f7c232"/>
      </linearGradient>
      <radialGradient id="oat-tone" cx="0.55" cy="0.5" r="0.7">
        <stop offset="0" stop-color="#c99a55"/>
        <stop offset="0.6" stop-color="#e0bf7d"/>
        <stop offset="1" stop-color="#f0e2bd"/>
      </radialGradient>
      <linearGradient id="silver-crimp" x1="0" y1="0" x2="1" y2="0">
        <stop offset="0" stop-color="#f2f2f2"/>
        <stop offset="0.3" stop-color="#c8c8c8"/>
        <stop offset="0.5" stop-color="#f7f7f7"/>
        <stop offset="0.75" stop-color="#b5b5b5"/>
        <stop offset="1" stop-color="#e6e6e6"/>
      </linearGradient>
    </defs>

    <path class="crimp-left" fill="#5a3020"
      d="M60 0 L0 0 L8 15 L0 30 L8 45 L0 60 L8 75 L0 90 L8 105 L0 120 L8 135 L0 150 L8 165 L0 180 L8 195 L0 210 L8 225 L0 240 L8 255 L0 270 L8 285 L0 300 L8 315 L0 330 L8 345 L0 360 L8 375 L0 390 L8 405 L0 420 L8 435 L0 450 L8 465 L0 470 L60 470 Z"/>
    <g stroke="#3a1c11" stroke-width="2" opacity="0.6">
      <line x1="22" y1="0" x2="22" y2="470"/>
      <line x1="36" y1="0" x2="36" y2="470"/>
      <line x1="50" y1="0" x2="50" y2="470"/>
    </g>

    <rect class="body" x="60" y="0" width="775" height="470" fill="var(--choc)"/>

    <rect x="0" y="0" width="260" height="470" fill="url(#chocolate-tone)" opacity="0.55"
      role="img" aria-label="Glossy chocolate pieces photograph"/>

    <polygon points="625,0 655,0 313,470 283,470" fill="url(#yellow-stripe)"/>
    <polygon points="679,0 829,0 530,470 352,470" fill="url(#orange-band)"/>

    <polygon class="tagline-band" points="0,258 665,258 636,304 0,304" fill="var(--band-red)"/>

    <polygon points="829,0 835,0 835,470 530,470" fill="url(#oat-tone)"
      role="img" aria-label="Window showing the oat and peanut bar inside"/>

    <g fill="none" stroke="var(--flavor)" stroke-width="4">
      <polyline points="6,334 14,344 6,354"/>
      <polyline points="22,334 30,344 22,354"/>
      <polyline points="38,334 46,344 38,354"/>
      <polyline points="54,334 62,344 54,354"/>
      <polyline points="70,334 78,344 70,354"/>
      <polyline points="86,334 94,344 86,354"/>
      <polyline points="102,334 110,344 102,354"/>
      <polyline points="118,334 126,344 118,354"/>
      <polyline points="134,334 142,344 134,354"/>
      <polyline points="150,334 158,344 150,354"/>
    </g>

    <path class="crimp-right" fill="url(#silver-crimp)"
      d="M835 0 L890 0 L882 15 L890 30 L882 45 L890 60 L882 75 L890 90 L882 105 L890 120 L882 135 L890 150 L882 165 L890 180 L882 195 L890 210 L882 225 L890 240 L882 255 L890 270 L882 285 L890 300 L882 315 L890 330 L882 345 L890 360 L882 375 L890 390 L882 405 L890 420 L882 435 L890 450 L882 465 L890 470 L835 470 Z"/>
    <g stroke="var(--silver-dark)" stroke-width="2" opacity="0.7">
      <line x1="852" y1="0" x2="852" y2="470"/>
      <line x1="866" y1="0" x2="866" y2="470"/>
    </g>
  </svg>

  <div class="logo condensed">VOLMBite</div>
  <div class="tagline">SUPER FOOD BAR</div>
  <div class="flavor">Flavor Peanut Chocolate Chip</div>
  <div class="protein-amount">14G</div>
  <div class="protein-label">Whey Protein</div>
</section>

</body>
</html>
```